Varlow's Electrical & Solar - Business Cards

I want my business card to stand out from the rest. I will provide my business name logo and my icon logo to be implemented onto the card.

On the front of the card, can i have the following. Just make it neat & professional please.

Dean Harrop
varlowselectrical@mailbox-example.net
0491 837 562
ABN: 41 269 507 813
License No. 582146K
FREE QUOTES
24/7 Emergency

On the back of the card, can I have "Our Services" and maybe add the V logo on the back in the background or something. Under "Our Services" I want the following:

LED Lighting Upgrades
Switches & Outlets
Smoke Alarms
Switchboard Upgrades
Fault Finding
Rewiring
New Builds
Test & Tagging
All Electrical Maintenance & Repairs

Can you guys add the instagram logo and next to it, put varlows_electrical

Can you guys also add the facebook logo and next to it put Varlow's Electrical & Solar. Make sure the instagram & facebook icon is in either white, green or black.

Also I have put down double sided, not sure why when i save it, it keeps going to single sided. I need my business card double sided.

New Customers

Dean Harrop varlowselectrical@mailbox-example.net 0491 837 562 ABN: 41 269 507 813 License No. 582146K FREE QUOTES 24/7 Emergency

• must be tidy, professional and appealing

```html
<!DOCTYPE html>
<html lang="en">
<head>
<meta charset="UTF-8">
<title>Varlow's Electrical &amp; Solar – Business Cards</title>
<link rel="stylesheet" href="https://fonts.googleapis.com/css2?family=Montserrat:wght@400;500;600;700&display=swap">
<style>
  :root {
    --backdrop: #7d6a52;
    --card: #1b1b1b;
    --green: #2b9e47;
    --green-bright: #3cb557;
    --white: #ffffff;
    --text: #f2f2f2;
  }
  * { box-sizing: border-box; margin: 0; padding: 0; }
  html, body {
    width: 900px; height: 1200px; overflow: hidden;
    background: var(--backdrop);
    font-family: "Montserrat", Arial, sans-serif;
  }
  .canvas { position: relative; width: 900px; height: 1200px; }
  .card {
    position: absolute; left: 78px; width: 744px; height: 442px;
    background: var(--card); border-radius: 28px;
    box-shadow: 0 10px 24px rgba(0,0,0,.35);
    overflow: hidden;
  }
  .card--front { top: 130px; }
  .card--back { top: 638px; }

  .holder-name {
    position: absolute; left: 29px; top: 86px;
    font-size: 29px; font-weight: 700; color: var(--green);
  }
  .contact-list { position: absolute; left: 30px; top: 154px; list-style: none; }
  .contact-list li {
    display: flex; align-items: center; gap: 6px;
    height: 30px; font-size: 17px; color: var(--text); font-weight: 400;
    white-space: nowrap;
  }
  .contact-list .contact-email { font-size: 15.5px; }
  .contact-list .label { color: var(--green); font-weight: 700; }
  .contact-list svg { flex: none; }
  .social-mark {
    flex: none; width: 17px; height: 17px; background: var(--green);
    margin-right: 3px;
  }
  .social-mark--round { border-radius: 50%; }
  .social-mark--square { border-radius: 3px; }
  .tagline {
    position: absolute; left: 29px; top: 344px;
    font-size: 17px; color: var(--text); letter-spacing: .2px;
  }

  .brand-mark {
    position: absolute; display: flex; align-items: center; justify-content: center;
    border: 10px solid var(--green-bright); border-radius: 50%;
    text-align: center; color: var(--green-bright); font-weight: 700;
    line-height: 1.25;
  }
  .card--front .brand-mark { left: 428px; top: 76px; width: 290px; height: 290px; font-size: 27px; }
  .card--back .brand-mark { left: 31px; top: 80px; width: 280px; height: 280px; font-size: 25px; }

  .services-divider {
    position: absolute; left: 333px; top: 70px; width: 2px; height: 300px;
    background: var(--green);
  }
  .services-title {
    position: absolute; left: 354px; top: 68px;
    font-size: 28px; font-weight: 700; color: var(--green);
  }
  .services-list { position: absolute; left: 355px; top: 113px; list-style: none; }
  .services-list li {
    position: relative; padding-left: 18px; height: 29.3px;
    font-size: 18.5px; color: var(--text);
  }
  .services-list li::before {
    content: ""; position: absolute; left: 0; top: 8px;
    width: 9px; height: 9px; border-radius: 50%; background: var(--green-bright);
  }
</style>
</head>
<body>
<main class="canvas">
  <section class="card card--front" aria-label="Business card front">
    <h1 class="holder-name">Dean Harrop</h1>
    <ul class="contact-list">
      <li>
        <svg width="18" height="16" viewBox="0 0 24 20" aria-hidden="true"><path fill="var(--green)" d="M2 6c0-3 4-5 10-5s10 2 10 5v2h-5V6c-2-1-8-1-10 0v2H2zM6 9h12l3 9H3z"/><circle cx="12" cy="13.5" r="2.5" fill="var(--card)"/></svg>
        <span>0491 837 562</span>
      </li>
      <li class="contact-email">
        <svg width="17" height="13" viewBox="0 0 20 14" aria-hidden="true"><rect width="20" height="14" rx="2" fill="var(--green)"/><path d="M1 1l9 7 9-7" fill="none" stroke="var(--card)" stroke-width="2"/></svg>
        <span>varlowselectrical@mailbox-example.net</span>
      </li>
      <li><span class="label">ABN:</span> <span>41 269 507 813</span></li>
      <li><span class="label">License No:</span> <span>582146K</span></li>
      <li><span class="social-mark social-mark--round" aria-hidden="true"></span><span>varlows_electrical</span></li>
      <li><span class="social-mark social-mark--square" aria-hidden="true"></span><span>Varlow's Electrical &amp; Solar</span></li>
    </ul>
    <p class="tagline">FREE QUOTES 24/7 Emergency</p>
    <div class="brand-mark">Varlow's<br>Electrical<br>&amp; Solar</div>
  </section>

  <section class="card card--back" aria-label="Business card back">
    <div class="brand-mark">Varlow's<br>Electrical<br>&amp; Solar</div>
    <div class="services-divider" aria-hidden="true"></div>
    <h2 class="services-title">Our Services</h2>
    <ul class="services-list">
      <li>LED Lighting Upgrades</li>
      <li>Switches &amp; Outlets</li>
      <li>Smoke Alarms</li>
      <li>Switchboard Upgrades</li>
      <li>Fault Finding</li>
      <li>Rewiring</li>
      <li>New Builds</li>
      <li>Test &amp; Tagging</li>
      <li>All Electrical Maintenance &amp; Repairs</li>
    </ul>
  </section>
</main>
</body>
</html>
```